Banner Ad in Spanish for Car Accident Law Firm in Miami Florida

I need a Banner Ad in Spanish Language. We are an Accident Law Firm in Miami, FL. We help injured people. I need a Banner Ad with a Vibrant Colorful Background to Stand Out. A Click-Able Call to Action is needed. We don't want to make the banner too crowded and we want the message to be simple to understand. We are looking for a skilled graphic designer to create a visually appealing banner ad for our YouTube marketing campaign. The required dimensions and format are:
1920 x 275
.png & .mp4

The Banner is for our Plaintiff’s Personal Injury Law Firm. We represent Spanish Speaking clients who are injured in CAR ACCIDENTS. As such the banner must include:
1. Our Firm Logo
2. Our Telephone# (305) 471-6023
3. Stock Photo of Car Crash
4. Photo of our attorney in office
5. The Words Abogados de Accidentes
The telephone number should be fairly large and stand out it is our call to action. The words Abogados de Accidentes should be close to our Logo to associate the two.

Target Market(s)

Car Accident Victims who speak Spanish

Industry/Entity Type

Legal, Law Firm.

Font styles to use
Sans Serif

Colors
59FF00
82FF00
B8FF75
E3FFCB
F4FFEA
F0912C
F2A743
F7CA91
FBE8D2
FDF5EE
6B429C
8869AF
B7A5CE
E3DAEB
F3F0F8

Requirements
Must have
• A bold background so that Banner Ad can be seen on mobile and against the screen being advertising against
Should not have
• Be too crowded. Hard to understand what it is for.

```html
<!DOCTYPE html>
<html lang="es">
<head>
<meta charset="utf-8">
<title>Abogados de Accidentes – Banner</title>
<link href="https://fonts.googleapis.com/css2?family=Fira+Sans:wght@500;600;700&display=swap" rel="stylesheet">
<style>
  :root {
    --navy: #262262;
    --navy-soft: #35307a;
    --violet: #5a52a0;
    --amber: #f7b23b;
    --amber-deep: #e89a1e;
    --ink: #262262;
    --paper: #ffffff;
    --suit: #7c8088;
  }
  * { box-sizing: border-box; margin: 0; padding: 0; }
  html, body { width: 763px; height: 1200px; overflow: hidden; background: var(--paper); }
  body { position: relative; font-family: "Fira Sans", Arial, sans-serif; }

  .format { position: absolute; left: 51px; width: 662px; background: var(--navy); }
  .format--wide { top: 49px; height: 372px; }
  .format--strip { top: 479px; height: 95px; }
  .size-label {
    position: absolute; left: 0; width: 763px; text-align: center;
    font-weight: 600; font-size: 13px; color: var(--ink); letter-spacing: .3px;
  }
  .size-label--wide { top: 434px; }
  .size-label--strip { top: 586px; }

  /* Large banner */
  .hero { position: absolute; left: 51px; top: 645px; width: 662px; height: 372px; background: var(--navy); overflow: hidden; }
  .hero__crash {
    position: absolute; left: 283px; top: 0; width: 379px; height: 372px;
    background: radial-gradient(ellipse at 70% 65%, #403a80 0%, #3a3478 35%, transparent 75%),
                linear-gradient(200deg, #5b53a2 0%, #3b3579 45%, var(--navy) 100%);
  }
  .hero__stripe { position: absolute; width: 40px; height: 360px; background: #2c286d; transform: rotate(-40deg); }
  .hero__attorney {
    position: absolute; left: 53px; top: 31px; width: 215px; height: 341px;
    border-radius: 90px 90px 0 0;
    background: linear-gradient(180deg, #c9a38e 0%, #c9a38e 22%, #8a8d94 24%, var(--suit) 100%);
  }
  .brand { position: absolute; display: flex; align-items: center; color: var(--paper); }
  .brand__mark { background: var(--paper); border-radius: 4px; }
  .brand__name { font-weight: 600; line-height: 1; letter-spacing: .5px; }
  .hero .brand { left: 302px; top: 46px; gap: 8px; }
  .hero .brand__mark { width: 36px; height: 36px; }
  .hero .brand__name { font-size: 19px; }
  .hero__title {
    position: absolute; left: 298px; top: 112px; color: var(--paper);
    font-weight: 600; font-size: 44px; line-height: 59px;
  }
  .cta { position: absolute; display: flex; align-items: center; }
  .cta__pill {
    background: var(--amber); color: var(--navy); font-weight: 700;
    border-radius: 0 6px 6px 0; white-space: nowrap;
  }
  .cta__icon {
    position: absolute; left: 0; border-radius: 50%; background: var(--navy);
    border: 2px solid var(--amber); display: flex; align-items: center; justify-content: center;
  }
  .hero .cta { left: 292px; top: 249px; }
  .hero .cta__pill { margin-left: 24px; padding: 5px 16px 5px 32px; font-size: 24px; }
  .hero .cta__icon { width: 50px; height: 50px; top: -5px; }

  /* Strip banner */
  .strip { position: absolute; left: 51px; top: 1053px; width: 662px; height: 95px; }
  .strip .brand { left: 15px; top: 34px; gap: 5px; color: var(--navy); }
  .strip .brand__mark { width: 24px; height: 24px; background: var(--navy); }
  .strip .brand__name { font-size: 12px; }
  .strip__band {
    position: absolute; left: 101px; top: 0; width: 561px; height: 95px; background: var(--navy); overflow: hidden;
    clip-path: polygon(0 0, 100% 0, 100% 100%, 0 100%, 0 100%, 4% 50%);
  }
  .strip__crash {
    position: absolute; right: 0; top: 0; width: 200px; height: 95px;
    background: linear-gradient(90deg, var(--navy) 0%, #3d377c 40%, #4e478f 100%);
  }
  .strip__attorney {
    position: absolute; left: 2px; top: 8px; width: 78px; height: 87px; border-radius: 30px 30px 0 0;
    background: linear-gradient(180deg, #c9a38e 0%, #c9a38e 28%, #8a8d94 30%, var(--suit) 100%);
  }
  .strip__title { position: absolute; left: 119px; top: 14px; color: var(--paper); font-weight: 600; font-size: 24px; white-space: nowrap; }
  .strip .cta { left: 204px; top: 56px; }
  .strip .cta__pill { margin-left: 14px; padding: 2px 8px 2px 20px; font-size: 14px; }
  .strip .cta__icon { width: 28px; height: 28px; top: -3px; }
</style>
</head>
<body>
  <div class="format format--wide"></div>
  <p class="size-label size-label--wide">1920x1080</p>
  <div class="format format--strip"></div>
  <p class="size-label size-label--strip">1920x275</p>

  <section class="hero">
    <div class="hero__crash" role="img" aria-label="Foto de un coche chocado con tinte violeta"></div>
    <div class="hero__stripe" style="left:20px;top:140px"></div>
    <div class="hero__stripe" style="left:60px;top:200px"></div>
    <div class="hero__attorney" role="img" aria-label="Foto del abogado en traje gris"></div>
    <div class="brand">
      <span class="brand__mark"></span>
      <span class="brand__name">ALVARADO LAW FIRM</span>
    </div>
    <h1 class="hero__title">Abogados de<br>Accidentes</h1>
    <a class="cta">
      <span class="cta__icon">
        <svg width="22" height="22" viewBox="0 0 24 24"><path fill="#f7b23b" d="M6.6 10.8a15.1 15.1 0 0 0 6.6 6.6l2.2-2.2c.3-.3.7-.4 1-.2 1.1.4 2.3.6 3.6.6.6 0 1 .4 1 1V20c0 .6-.4 1-1 1A17 17 0 0 1 3 4c0-.6.4-1 1-1h3.5c.6 0 1 .4 1 1 0 1.3.2 2.5.6 3.6.1.3 0 .7-.2 1z"/></svg>
      </span>
      <span class="cta__pill">(305) 471-6023</span>
    </a>
  </section>

  <section class="strip">
    <div class="brand">
      <span class="brand__mark"></span>
      <span class="brand__name">ALVARADO</span>
    </div>
    <div class="strip__band">
      <div class="strip__crash" role="img" aria-label="Foto de un coche chocado"></div>
      <div class="strip__attorney" role="img" aria-label="Foto del abogado en traje gris"></div>
      <p class="strip__title">Abogados de Accidentes</p>
      <a class="cta">
        <span class="cta__icon">
          <svg width="13" height="13" viewBox="0 0 24 24"><path fill="#f7b23b" d="M6.6 10.8a15.1 15.1 0 0 0 6.6 6.6l2.2-2.2c.3-.3.7-.4 1-.2 1.1.4 2.3.6 3.6.6.6 0 1 .4 1 1V20c0 .6-.4 1-1 1A17 17 0 0 1 3 4c0-.6.4-1 1-1h3.5c.6 0 1 .4 1 1 0 1.3.2 2.5.6 3.6.1.3 0 .7-.2 1z"/></svg>
        </span>
        <span class="cta__pill">(305) 471-6023</span>
      </a>
    </div>
  </section>
</body>
</html>
```